Construction training company needs a workshop invitation template

We need an invitation template for our professional development workshops we run for construction companies.
We would like to see designs that use the colors in our Framehold Sentinel Logo.
A simple, clean design with a lot of white space would be preferred.
No reverse text or italics.
The template should be done in Adobe Illustrator.

• Reverse text or italics

```html
<!DOCTYPE html>
<html lang="en">
<head>
<meta charset="utf-8">
<title>Framehold Sentinel – Workshop Invitation</title>
<link rel="stylesheet" href="https://fonts.googleapis.com/css2?family=Arimo:wght@400;700&family=Raleway:wght@300&family=Roboto:wght@300;400&family=Crimson+Pro:wght@400&display=swap">
<style>
  :root{
    --lime:#b7d433;
    --green:#5aa82f;
    --deep:#0b1b1d;
    --forest:#0a4a2e;
    --ink:#2a2a2a;
    --paper:#ffffff;
  }
  *{box-sizing:border-box;margin:0;padding:0}
  html,body{width:1200px;height:900px;overflow:hidden;background:var(--paper)}
  .stage{position:relative;width:1200px;height:900px}
  .card{position:absolute;left:316px;width:609px;height:429px;background:var(--paper);overflow:hidden;
        box-shadow:0 1px 4px rgba(0,0,0,.12)}
  .card--front{top:16px}
  .card--back{top:463px;height:428px}
  .card svg.shapes{position:absolute;inset:0}
  .abs{position:absolute}

  .brand{display:flex;align-items:center;gap:10px}
  .brand__mark{width:34px;height:34px;background:var(--green);flex:none}
  .brand__name{font-family:"Arimo",sans-serif;font-weight:700;color:var(--ink);font-size:18px;line-height:22px}

  .front-copy{left:19px;top:116px;width:284px;font-family:"Roboto",sans-serif;font-weight:300;
              font-size:16px;line-height:19.6px;color:var(--ink)}
  .front-copy p{margin-bottom:19.6px}
  .front-copy .free{font-family:"Arimo",sans-serif;font-weight:700;font-size:16.5px;line-height:19.6px;margin-bottom:38px}

  .invite-title{right:14px;top:16px;font-family:"Raleway",sans-serif;font-weight:300;color:var(--lime);font-size:40px;line-height:44px;letter-spacing:-1px}
  .invite-lead{right:14px;top:66px;font-family:"Roboto",sans-serif;font-weight:300;color:#fff;font-size:20px;letter-spacing:-.3px}
  .event-name{right:23px;top:101px;text-align:right;font-family:"Arimo",sans-serif;font-weight:700;color:#fff;font-size:30px;line-height:34.5px}
  .event-rule{left:592px;top:101px;width:2px;height:107px;background:var(--lime)}
  .event-when{right:14px;top:228px;text-align:right;font-family:"Arimo",sans-serif;font-weight:700;color:var(--deep);font-size:14px;line-height:17.5px}

  .back-head{left:33px;top:24px;font-family:"Arimo",sans-serif;font-weight:700;color:var(--lime);font-size:23px;line-height:27px}
  .topics{top:98px;list-style:none;font-family:"Crimson Pro",serif;font-size:13.3px;line-height:14.8px;color:var(--ink)}
  .topics li{position:relative;padding-left:9px;margin-bottom:3.5px;white-space:nowrap}
  .topics li::before{content:"·";position:absolute;left:0;top:0}
  .topics--left{left:29px;width:272px}
  .topics--right{left:319px;width:290px}
  .topics--right li{line-height:18px;margin-bottom:0}
  .divider{left:303px;top:92px;width:2px;height:210px;background:linear-gradient(to right,rgba(0,0,0,.08),rgba(0,0,0,0))}

  .cta{left:343px;top:341px;font-family:"Arimo",sans-serif;font-weight:700;color:var(--deep)}
  .cta__note{font-size:9.5px;line-height:12px}
  .cta__call{font-size:18px;line-height:20px}
</style>
</head>
<body>
<main class="stage">

  <section class="card card--front">
    <svg class="shapes" width="609" height="429" viewBox="0 0 609 429">
      <defs>
        <linearGradient id="darkPanel" x1="0" y1="1" x2="1" y2="0">
          <stop offset="0" stop-color="#0b1b1d"/><stop offset=".55" stop-color="#0c2a24"/><stop offset="1" stop-color="#0a4a2e"/>
        </linearGradient>
        <linearGradient id="limeGreen" x1="0" y1="0" x2="1" y2="0">
          <stop offset="0" stop-color="#b7d433"/><stop offset="1" stop-color="#6db62f"/>
        </linearGradient>
        <radialGradient id="faint" cx=".5" cy=".5" r=".5">
          <stop offset="0" stop-color="#eef3ea"/><stop offset="1" stop-color="#ffffff" stop-opacity="0"/>
        </radialGradient>
      </defs>
      <rect role="img" aria-label="Faint brand decoration" x="0" y="300" width="200" height="129" fill="url(#faint)"/>
      <polygon points="548,320 609,290 609,429 592,429" fill="var(--green)"/>
      <g stroke="#fff" stroke-width=".7" opacity=".8">
        <line x1="545" y1="334" x2="595" y2="429"/><line x1="553" y1="330" x2="603" y2="429"/>
        <line x1="561" y1="326" x2="609" y2="418"/><line x1="569" y1="322" x2="609" y2="402"/>
      </g>
      <g stroke="#999" stroke-width=".5">
        <line x1="525" y1="345" x2="570" y2="429"/><line x1="531" y1="342" x2="576" y2="429"/><line x1="537" y1="339" x2="582" y2="429"/>
      </g>
      <polygon points="232,0 258,0 442,360 428,378" fill="var(--lime)"/>
      <polygon points="440,382 609,290 609,304 452,384" fill="url(#limeGreen)"/>
      <path d="M248,0 L609,0 L609,290 L447,377 Q432,384 424,368 Z" fill="url(#darkPanel)"/>
      <path d="M387,222 L609,222 L609,284 L412,284 Q404,284 400,276 L382,232 Q380,222 387,222 Z" fill="url(#limeGreen)"/>
      <rect x="0" y="418" width="609" height="11" fill="var(--lime)"/>
    </svg>

    <div class="brand abs" style="left:19px;top:50px">
      <span class="brand__mark"></span>
      <span class="brand__name">Framehold Sentinel</span>
    </div>

    <div class="front-copy abs">
      <p>The case study at this workshop will be the Kestrel Build Co project at 14 Harlow St, Bayfield</p>
      <p>Enjoy some good coffee at the start and awesome food for lunch at the end - all compliments of Kestrel Build Co</p>
      <p class="free">AND THERE’S NO CHARGE FOR ATTENDING!</p>
      <p>See reverse side for more info</p>
    </div>

    <div class="invite-title abs">You’re Invited!</div>
    <div class="invite-lead abs">Kestrel Build Co invite you to a</div>
    <h1 class="event-name abs">PROFESSIONAL<br>DEVELOPMENT<br>WORKSHOP</h1>
    <span class="event-rule abs"></span>
    <div class="event-when abs">June 7, 2021 | 7AM to 12NN<br>At (address of venue<br>inserted here)</div>
  </section>

  <section class="card card--back">
    <svg class="shapes" width="609" height="428" viewBox="0 0 609 428">
      <defs>
        <radialGradient id="faint2" cx=".5" cy=".5" r=".5">
          <stop offset="0" stop-color="#eef3ea"/><stop offset="1" stop-color="#ffffff" stop-opacity="0"/>
        </radialGradient>
        <linearGradient id="limeGreen2" x1="0" y1="0" x2="1" y2="0">
          <stop offset="0" stop-color="#b7d433"/><stop offset="1" stop-color="#8cc63f"/>
        </linearGradient>
      </defs>
      <rect role="img" aria-label="Faint brand decoration" x="420" y="10" width="189" height="150" fill="url(#faint2)"/>
      <polygon points="0,380 0,428 22,428" fill="var(--green)"/>
      <g stroke="#aaa" stroke-width=".5">
        <line x1="0" y1="330" x2="45" y2="428"/><line x1="0" y1="316" x2="51" y2="428"/><line x1="0" y1="302" x2="57" y2="428"/>
      </g>
      <polygon points="30,428 100,392 120,428" fill="var(--lime)"/>
      <path d="M38,428 L98,396 Q108,390 114,400 L126,428 Z" fill="var(--deep)"/>
      <path d="M322,334 L609,334 L609,384 L338,384 Q330,384 327,376 L316,344 Q314,334 322,334 Z" fill="url(#limeGreen2)"/>
    </svg>

    <h2 class="back-head abs">THIS IS A LIVE ACTION WORKSHOP WHERE YOU<br>PARTICIPATE IN AND LEARN ABOUT</h2>

    <span class="divider abs"></span>
    <ul class="topics topics--left abs">
      <li>How to set up a smart schedule for a<br>construction project</li>
      <li>How to get clarity on the building work to<br>be done, using a 3D model</li>
      <li>Getting everybody onto the same page</li>
      <li>Solving construction headaches before<br>they happen</li>
      <li>Getting the information you need to make you<br>more efficient and effective</li>
      <li>How to get more satisfaction out of your work</li>
      <li>Delivering projects in less time and lower costs</li>
      <li>Achieving better quality work</li>
    </ul>
    <ul class="topics topics--right abs">
      <li>Ensuring a high level of worksite safety</li>
      <li>Developing stronger relationships withing<br>the workforce</li>
      <li>How smart collaboration can improve things<br>for everybody</li>
      <li>Transforming workplace culture and reducing the<br>mental health issues in the construction industry</li>
      <li>Reducing rework and warranty work</li>
      <li>Creating better results, with less time, effort<br>and cost</li>
      <li>Boosting customer satisfaction and referrals</li>
    </ul>

    <div class="brand abs" style="left:32px;top:352px">
      <span class="brand__mark"></span>
      <span class="brand__name">Framehold Sentinel</span>
    </div>

    <div class="cta abs">
      <div class="cta__note">LIMITED SEATS ONLY SO BOOK YOUR SPOT TODAY!</div>
      <div class="cta__call">CALL MAREN on 0411 555 019</div>
    </div>
  </section>

</main>
</body>
</html>
```